Corrigan's Irish Pub Menu Design

New menu design for Corrigan's Irish Pub prefer someone with menu design experience. Menu items are attached and I'll need working files to make updates. The design should be 8.5"x14" 1 cover page and 3 page menu if possible or 4 page menu if not with a Header on the first page this is for print and web. Please include the new logo and it should be in a traditional Irish Pub style. When complete please send a proof for markup (watermark is fine just want to markup and proof) and I'll send back for revisions.
Colors
Designer to choose colors to be used in the design.
Look and feel
Each slider illustrates characteristics of the customer's brand and the style your logo design should communicate.

```html
<!DOCTYPE html>
<html lang="en">
<head>
<meta charset="utf-8">
<title>Corrigan's Irish Pub — Menu Spread</title>
<link rel="stylesheet" href="https://fonts.googleapis.com/css2?family=Marcellus&family=Josefin+Sans:wght@300;400;600&display=swap">
<style>
  :root {
    --backdrop: #e8e9ea;
    --paper: #f1f2f3;
    --pub-green: #1c3a2c;
    --ink: #1f3328;
    --photo-dark: #2a1d14;
    --photo-warm: #8a5a2c;
    --photo-leaf: #3f7a32;
  }
  * { box-sizing: border-box; margin: 0; padding: 0; }
  html, body { width: 1200px; height: 1200px; overflow: hidden; background: var(--backdrop); }
  .spread {
    position: absolute; left: 30px; top: 130px;
    width: 1140px; height: 940px; display: flex;
  }
  .panel { position: relative; width: 570px; height: 940px; display: flex; }
  .photo { width: 168px; height: 100%; }
  .photo--left {
    background: linear-gradient(180deg, var(--photo-dark) 0%, #5a3a1e 22%, var(--photo-warm) 45%, #b08a4a 60%, var(--photo-leaf) 82%, #2f5a26 100%);
  }
  .photo--right {
    background: linear-gradient(180deg, #1b1a1c 0%, #3b2a22 20%, #9a7a52 35%, #c2945a 55%, var(--photo-leaf) 78%, #2d5526 100%);
  }
  .spine-bar { width: 5px; height: 100%; background: var(--pub-green); }
  .page { position: relative; flex: 1; height: 100%; background: var(--paper); color: var(--ink); }
  .page--left { box-shadow: inset -18px 0 22px -18px rgba(0,0,0,.18); }

  .section-title {
    position: absolute; left: 0; right: 0; text-align: center;
    font-family: "Marcellus", serif; color: var(--pub-green);
  }
  .section-title--large { top: 122px; font-size: 48px; letter-spacing: 2px; }
  .section-title--medium { font-size: 24px; letter-spacing: 0.5px; }
  .section-note {
    position: absolute; left: 0; right: 0; top: 83px; text-align: center;
    font-family: "Josefin Sans", sans-serif; font-size: 12px; letter-spacing: 0.5px;
  }

  .item { position: absolute; left: 29px; right: 28px; }
  .item__head {
    display: flex; justify-content: space-between; align-items: baseline;
    font-family: "Marcellus", serif; font-size: 23px; color: var(--pub-green); letter-spacing: 0.5px;
  }
  .item__head small { font-size: 18px; letter-spacing: 1px; }
  .item__rule { width: 82px; height: 3px; background: var(--pub-green); margin-top: 6px; }
  .item__desc {
    margin-top: 18px; font-family: "Josefin Sans", sans-serif; font-size: 12.2px;
    line-height: 15.5px; letter-spacing: 0.4px;
  }
  .page--right .item { left: 30px; right: 36px; }

  .entrees { position: absolute; left: 30px; right: 28px; top: 677px; }
  .entree {
    display: flex; align-items: baseline;
    font-family: "Josefin Sans", sans-serif; font-weight: 300; font-size: 16px;
    letter-spacing: 0.8px; height: 33.5px;
  }
  .entree__leader { flex: 1; border-bottom: 1.5px dotted var(--ink); margin: 0 6px; transform: translateY(-4px); }
  .entree__desc {
    font-family: "Josefin Sans", sans-serif; font-weight: 300; font-size: 11px;
    line-height: 15.5px; letter-spacing: 0.8px; margin: -14px 0 14px; width: 300px;
  }
</style>
</head>
<body>
<main class="spread">
  <section class="panel">
    <div class="photo photo--left" role="img" aria-label="Photo of a pint of stout beside a sandwich with cucumber and lettuce"></div>
    <div class="spine-bar"></div>
    <div class="page page--left">
      <h1 class="section-title section-title--large">WRAPS</h1>

      <article class="item" style="top:219px">
        <div class="item__head"><span><small>the</small> CHICKEN WRAP</span><span>12</span></div>
        <div class="item__rule"></div>
        <p class="item__desc">Grilled or Blackend Chicken, Lettuce, Tomato,<br>Red Onion, Applewood Bacon and a Parmesan Ranch</p>
      </article>
      <article class="item" style="top:337px">
        <div class="item__head"><span><small>the</small> TURKEY WRAP</span><span>12</span></div>
        <div class="item__rule"></div>
        <p class="item__desc">Smoked Turkey, Swiss Cheese, Spinach, Tomato,<br>Applewood Bacon, Candled Whiskey Walnuts,<br>Cranberry Aioli</p>
      </article>
      <article class="item" style="top:471px">
        <div class="item__head"><span><small>the</small> HADDOCK WRAP</span><span>13</span></div>
        <div class="item__rule"></div>
        <p class="item__desc">Grilled or Blackend Haddock, Lettuce, Tomato,<br>Cheddar Cheese and Remoulade</p>
      </article>
      <article class="item" style="top:589px">
        <div class="item__head"><span><small>the</small> SALMON WRAP</span><span>13</span></div>
        <div class="item__rule"></div>
        <p class="item__desc">Grilled or Blackend Haddock, Spinach, Tomato,<br>Scallions, Gouda Cheese, and Garlic and Thyme Aioli</p>
      </article>
      <article class="item" style="top:707px">
        <div class="item__head"><span><small>the</small> VEGGIE WRAP</span><span>12</span></div>
        <div class="item__rule"></div>
        <p class="item__desc">Artichokes, Spinach, Tomato, Cucumbers,<br>Red Onion, Mozz Cheese and a Roasted Red Pepper Aioli</p>
      </article>
    </div>
  </section>

  <section class="panel">
    <div class="photo photo--right" role="img" aria-label="Photo of a pressed panini sandwich on a wooden board with salad greens"></div>
    <div class="spine-bar"></div>
    <div class="page page--right">
      <h2 class="section-title section-title--medium" style="top:44px">10″ FLAT BREADS</h2>
      <p class="section-note">With a Gluten Free Cauliflour Crust</p>

      <article class="item" style="top:123px">
        <div class="item__head"><span>BBQ PORK</span><span>12</span></div>
        <div class="item__rule"></div>
        <p class="item__desc">Corrigan's BBQ Sauce, Pulled Mojo Pork, Sliced Apples,<br>Blue Cheese Crumbles and Mozz Cheese</p>
      </article>
      <article class="item" style="top:241px">
        <div class="item__head"><span>BUFFALO CHICKEN</span><span>12</span></div>
        <div class="item__rule"></div>
        <p class="item__desc">Dunmore Buffalo Sauce, Pulled Chicken, Diced Celery,<br>Scallions, Blue Cheese, Crumbles and Mozz Cheese</p>
      </article>
      <article class="item" style="top:375px">
        <div class="item__head"><span>IRISH BANGER</span><span>12</span></div>
        <div class="item__rule"></div>
        <p class="item__desc">Stout Grain Mustard Sauce, Bangers, Applewood Bacon,<br>Onions, Roasted Red Pepper and Smoked Gouda Cheese</p>
      </article>
      <article class="item" style="top:493px">
        <div class="item__head"><span>VEGGIE PIE</span><span>12</span></div>
        <div class="item__rule"></div>
        <p class="item__desc">Whiskeyed Fig Cream Cheese Sauce, Spinach, Artichokes,<br>Cherry Tomatoes, Cucumber, Scallions, Parmesan<br>and Smoked Gouda Cheese</p>
      </article>

      <h2 class="section-title section-title--medium" style="top:637px">ENTREE’S</h2>
      <div class="entrees">
        <div class="entree"><span>BANGERS AND MASH</span><span class="entree__leader"></span><span>15</span></div>
        <div class="entree"><span>SHEPHERD’S PIE</span><span class="entree__leader"></span><span>13</span></div>
        <div class="entree"><span>FISH AND CHIPS</span><span class="entree__leader"></span><span>13</span></div>
        <div class="entree"><span>CORNED BEEF AND CABBAGE</span><span class="entree__leader"></span><span>13</span></div>
        <p class="entree__desc">Dunmore Pulled Corned Beef with Caraway Cabbage and Smoked Goud Mashed Potatoes. Served with Stout Mustard</p>
        <div class="entree"><span>GARLIC BREAKFAST PLATE</span><span class="entree__leader"></span><span>12</span></div>
      </div>
    </div>
  </section>
</main>
</body>
</html>
```